Help develop the "Breezy Brew" Logo & Can Design for new beer!

We're a new beer being produced in the Caribbean. Thus looking for a beer logo design that
1) capitalizes on the word "Breezy" for further beer lines that spin off of this first one. EXAMPLES OF OTHER BEER NAMES TO BE PRODUCED THAT HAVE TO HAVE TIE IN TO ORIGINAL DESIGN: "One Breezy Brew", "Sunny Pelican Wobble Brew" "Ramblefoot Breezy Brew" "Wharrya doin' Breezy Brew" "Bout now for Breezy Brew", "Tamarna Breezy Brew" etc etc etc,

2) has unique visual impact,
3) Logo has to be usable across variety of mediums,
4) 4 color maximum,
5) Island art feel,
6) Breezy Brew needs to convey a since of "lightness and slight tongue-in-cheek or off beat humor"...but not overwhelming,
7) Each subsequent label names (see above) needs to be distinctly color coded, but connects to the overarching theme of the brand with distinctive interpretations of each beer’s name.
8) Needs to be BOLD in statement and color.

You can get inspiration from some of these logo's. Follow this link: http://www.quorvelstudio.com/vintage-logos/
or http://www.tindralcrate.com/2014/12/30-beers-for-30-years-2001-to-2006.html

Also see attached files for inspiration!!!

Reason: We've extended the deadline for this project! Thus submit any new designs sooner than later. Thanks!

Target Market(s)

Male: Wear jeans & baseball cap, Played H.S. sports, Hunts/fish/golfDrive a truck or SUV, Work a blue collar job, Like working in the garage or on the landLike football/basketball/baseball, Are married high school sweetheart and have childrenAre from southern states...or wished they were, Chews tobacco or smokeDrink beerFemale: Attended college/community collegeAre married with kidsRide motorcycles, 4x4, ATV’sDrive Trucks or vansFish/camp/garden/sewDo craftsDrink beerGets manicures/pedicuresWears jewelry & jeans

Logo Text

Breezy Brew

Logo styles of interest
Emblem Logo
Pictorial/Combination Logo
Abstract Logo
Character Logo
Wordmark Logo
Requirements
Must have
• Eye catching & readable shelf presentation. Non-Standard art. High definition. Bold Statement. Clear design elements, various color options, High color contrast (like attached files) are needed for visual impact. Simple elements that conveys essence of the brand.
• You are designing the whole "beer can" logo elements, not just the the main logo. Things like background and side panels. Back panel for ingredients and messages to be added to. This is an "overall" can design, not just a single logo design.
• MUST HAVE THESE WORDS/SENTENCES/SECTIONS:
• Sentences: Our Breezy ales and lagers are handcrafted with some of the best ingredients the Caribbean has to offer!
• Section: So, Why Do we use can's?
• Can's eliminate potential light damage, reduce the risk of oxidation are lighter and chill quicker. Can be enjoyed on beaches and make for great recycling and table art. Plus they are the most recycled and eco-friendly material we can use. Breezy!
• BREWED AND BOTTLED/PACKED BY:
• IMPORTED BY
• ALCOHOL (ALC) ______% BY VOLUME (VOL)
• Recyclable
• GOVERNMENT WARNING:
• (1) According to the Surgeon General, women should not drink alcoholic beverages during pregnancy because of the risk of birth defects. (2) Consumption of
• alcoholic beverages impairs your ability to drive a car or operate machinery, and may cause health problems.
• Description: (This will change from beer to beer but this is good example of type language we would be using. "This Breezy Brew has a pletheria of Island goodness (there are hints of passion fruit, mango, and pineapple) along with some pleasant bitterness IPAs are known for. We can honestly say these sweet and savory flavors pair perfectly with this beer and you'll get a kick out of the IPA notes too!"
Should not have
• nudity, graphic language, skulls, flames,

```html
<!DOCTYPE html>
<html lang="en">
<head>
<meta charset="utf-8">
<title>Breezy Brew – Can Label Range</title>
<link rel="stylesheet" href="https://fonts.googleapis.com/css2?family=Josefin+Sans:wght@600;700&display=swap">
<style>
  :root {
    --stage-light: #f4f5f6;
    --stage-dark: #c9ccd0;
    --label-bg: #e4f3ef;
    --label-edge: #d3ebe5;
    --ink-brown: #3b1f0e;
    --ink-teal: #2a9aa0;
    --ink-orange: #e8870b;
    --ipa-dark: #11676b;
    --ipa-light: #46d6d4;
    --lager-dark: #d75a00;
    --lager-light: #ffc21a;
    --imperial-dark: #2a1306;
    --imperial-light: #7a4317;
    --palm-tint: rgba(120, 170, 160, 0.18);
  }
  * { box-sizing: border-box; margin: 0; padding: 0; }
  html, body { width: 1200px; height: 960px; overflow: hidden; }
  body {
    background: radial-gradient(ellipse at 50% 45%, var(--stage-light) 0%, #e3e5e8 55%, var(--stage-dark) 100%);
    font-family: "Josefin Sans", sans-serif;
    position: relative;
  }
  .range { position: absolute; top: 130px; left: 137px; display: flex; gap: 48px; }
  .label-wrap {
    width: 272px; height: 587px;
    display: flex; flex-direction: column;
  }
  .band { height: 90px; }
  .band--bottom { height: 110px; }
  .label-wrap--ipa .band { background: linear-gradient(90deg, var(--ipa-dark), var(--ipa-light) 30%, var(--ipa-dark) 55%, var(--ipa-light) 80%, var(--ipa-dark)); }
  .label-wrap--lager .band { background: linear-gradient(90deg, var(--lager-dark), var(--lager-light) 30%, var(--lager-dark) 55%, var(--lager-light) 80%, var(--lager-dark)); }
  .label-wrap--imperial .band { background: linear-gradient(90deg, var(--imperial-dark), var(--imperial-light) 30%, var(--imperial-dark) 55%, var(--imperial-light) 80%, var(--imperial-dark)); }

  .label {
    flex: 1; position: relative;
    background: linear-gradient(90deg, var(--label-edge), var(--label-bg) 25%, #f4fbf9 50%, var(--label-bg) 75%, var(--label-edge));
    text-align: center;
  }
  .palm-decor {
    position: absolute; top: 40px; width: 40px; height: 230px;
    background: linear-gradient(180deg, var(--palm-tint), transparent);
    border-radius: 20px;
  }
  .palm-decor--left { left: 0; }
  .palm-decor--right { right: 0; }

  .brand {
    position: absolute; top: 60px; left: 50%; transform: translateX(-50%);
    width: 170px; height: 220px;
    display: flex; flex-direction: column; align-items: center; justify-content: center; gap: 14px;
  }
  .brand-name {
    font-weight: 700; font-size: 30px; line-height: 1.05; letter-spacing: 1px;
    color: var(--ink-brown);
  }
  .brand-dot {
    width: 24px; height: 24px; border-radius: 50%;
    background: var(--ink-brown);
  }

  .beer-style {
    position: absolute; top: 285px; left: 0; right: 0;
    font-weight: 700; font-size: 17px; letter-spacing: 2.5px;
  }
  .beer-note {
    position: absolute; top: 307px; left: 0; right: 0;
    font-weight: 700; font-size: 9px; letter-spacing: 1.5px;
  }
  .abv {
    position: absolute; top: 325px; left: 50%; transform: translateX(-50%);
    font-weight: 700; color: #335f62; font-size: 10px; letter-spacing: 2px;
    white-space: nowrap;
  }
  .abv strong { font-size: 19px; letter-spacing: 0.5px; }
  .volume {
    position: absolute; top: 346px; left: 50%; transform: translateX(-50%);
    width: 118px; border-top: 1px solid #335f62; padding-top: 3px;
    font-weight: 700; font-size: 8px; letter-spacing: 2px; color: #335f62;
  }

  .label-wrap--ipa .beer-style { color: var(--ink-orange); }
  .label-wrap--ipa .beer-note { color: var(--ink-teal); }
  .label-wrap--ipa .abv strong { color: var(--ink-teal); }
  .label-wrap--lager .beer-style { color: var(--ink-teal); }
  .label-wrap--lager .beer-note { color: var(--ink-orange); }
  .label-wrap--lager .abv strong { color: var(--ink-orange); }
  .label-wrap--imperial .beer-style { color: var(--ink-orange); }
  .label-wrap--imperial .beer-note { color: var(--ink-brown); }
  .label-wrap--imperial .abv strong { color: var(--ink-brown); }
</style>
</head>
<body>
  <main class="range">
    <section class="label-wrap label-wrap--ipa">
      <div class="band band--top"></div>
      <div class="label">
        <div class="palm-decor palm-decor--left" role="img" aria-label="Faint palm tree silhouettes"></div>
        <div class="palm-decor palm-decor--right" role="img" aria-label="Faint palm tree silhouettes"></div>
        <div class="brand"><span class="brand-name">BREEZY<br>BREW</span><span class="brand-dot"></span></div>
        <h2 class="beer-style">INDIA PALE ALE</h2>
        <p class="beer-note">SHORT DESCRIPTION HERE</p>
        <p class="abv">ALC <strong>4.8%</strong> VOL</p>
        <p class="volume">12FL.OZ/355ML</p>
      </div>
      <div class="band band--bottom"></div>
    </section>

    <section class="label-wrap label-wrap--lager">
      <div class="band band--top"></div>
      <div class="label">
        <div class="palm-decor palm-decor--left" role="img" aria-label="Faint palm tree silhouettes"></div>
        <div class="palm-decor palm-decor--right" role="img" aria-label="Faint palm tree silhouettes"></div>
        <div class="brand"><span class="brand-name">BREEZY<br>BREW</span><span class="brand-dot"></span></div>
        <h2 class="beer-style">AMERICAN LAGER</h2>
        <p class="beer-note">SHORT DESCRIPTION HERE</p>
        <p class="abv">ALC <strong>4.8%</strong> VOL</p>
        <p class="volume">12FL.OZ/355ML</p>
      </div>
      <div class="band band--bottom"></div>
    </section>

    <section class="label-wrap label-wrap--imperial">
      <div class="band band--top"></div>
      <div class="label">
        <div class="palm-decor palm-decor--left" role="img" aria-label="Faint palm tree silhouettes"></div>
        <div class="palm-decor palm-decor--right" role="img" aria-label="Faint palm tree silhouettes"></div>
        <div class="brand"><span class="brand-name">BREEZY<br>BREW</span><span class="brand-dot"></span></div>
        <h2 class="beer-style">IMPERIAL IPA</h2>
        <p class="beer-note">SHORT DESCRIPTION HERE</p>
        <p class="abv">ALC <strong>4.8%</strong> VOL</p>
        <p class="volume">12FL.OZ/355ML</p>
      </div>
      <div class="band band--bottom"></div>
    </section>
  </main>
</body>
</html>
```